Bodywork Quietude Business Card Design

I want to create a very elegant and sophisticated two sided business card for my massage practice (www.bodyworkquietude.net). I have attached the logo and a PDF with some ideas down for the back of the card but I am open to suggestions. I will want to tie in a post card and flyer to the card later.
Similar colors to website would be great.
Target Market(s)
High end clientele, people looking for a sophisticated spa experience.
Industry/Entity Type
Massage
Contact Information for Business Card
Bodywork Quietude
7318 Larkspur Ave S, Suite 305
Lakemont, WA 98140
(206) 555-0147
www.bodyworkquietude.net
Look and feel

```html
<!DOCTYPE html>
<html lang="en">
<head>
<meta charset="utf-8">
<title>Bodywork Quietude Business Card</title>
<link rel="stylesheet" href="https://fonts.googleapis.com/css2?family=Cinzel:wght@400&family=Source+Sans+3:wght@400&display=swap">
<style>
  :root {
    --backdrop: #2e2e2e;
    --card-light: #e6e2dc;
    --card-dark: #1f3a48;
    --ink-navy: #1e3442;
    --ink-body: #2f3a42;
    --ink-muted: #3f5260;
    --silver: #d9dde0;
  }
  * { margin: 0; padding: 0; box-sizing: border-box; }
  html, body {
    width: 1200px; height: 600px; overflow: hidden;
    background: var(--backdrop);
  }
  .canvas {
    position: relative; width: 1200px; height: 600px;
  }
  .card {
    position: absolute; top: 164px;
    width: 466px; height: 272px;
    border-radius: 14px;
  }
  .card--front { left: 123px; background: var(--card-light); }
  .card--back { left: 613px; background: var(--card-dark); }

  .brand-name {
    font-family: "Cinzel", serif;
    font-weight: 400;
    white-space: nowrap;
  }
  .card--front .brand-name {
    position: absolute; right: 28px; top: 52px;
    font-size: 15px; color: var(--ink-navy);
  }
  .card--back .brand-name {
    position: absolute; left: 0; right: 0; top: 116px;
    text-align: center; font-size: 22px; color: var(--silver);
    letter-spacing: 0.4px;
  }

  .holder-name {
    position: absolute; left: 28px; top: 146px;
    font-family: "Cinzel", serif; font-size: 19px;
    color: var(--ink-body);
  }
  .holder-title {
    position: absolute; left: 28px; top: 170px;
    font-family: "Source Sans 3", sans-serif; font-size: 12px;
    color: var(--ink-muted);
  }
  .divider {
    position: absolute; left: 22px; width: 418px; top: 194px;
    height: 2px; background: var(--ink-navy);
  }
  .contact {
    position: absolute; left: 28px; right: 26px;
    font-family: "Source Sans 3", sans-serif; font-size: 12.5px;
    color: var(--ink-body);
    display: flex; justify-content: space-between; align-items: center;
  }
  .contact--row1 { top: 202px; }
  .contact--row2 { top: 225px; }
  .contact-item { display: flex; align-items: center; gap: 4px; }
  .indent { padding-left: 11px; }
  .icon { width: 11px; height: 11px; fill: var(--ink-muted); }
</style>
</head>
<body>
<div class="canvas">
  <section class="card card--front">
    <div class="brand-name">Bodywork Quietude</div>
    <div class="holder-name">Your Name</div>
    <div class="holder-title">Job Title</div>
    <div class="divider"></div>
    <div class="contact contact--row1">
      <span class="contact-item">
        <svg class="icon" viewBox="0 0 12 12" aria-hidden="true"><path d="M6 0a4 4 0 0 0-4 4c0 3 4 8 4 8s4-5 4-8a4 4 0 0 0-4-4zm0 5.6A1.6 1.6 0 1 1 6 2.4a1.6 1.6 0 0 1 0 3.2z"/></svg>
        7318 Larkspur Ave S, Suite 305
      </span>
      <span class="contact-item">
        (206) 555-0147
        <svg class="icon" viewBox="0 0 12 12" aria-hidden="true"><path d="M1 4c0-1.5 2-2.5 5-2.5s5 1 5 2.5v1H8.5V4h-5v1H1zM3 6h6l1.5 4.5h-9zM6 7a1.3 1.3 0 1 0 0 2.6A1.3 1.3 0 0 0 6 7z"/></svg>
      </span>
    </div>
    <div class="contact contact--row2">
      <span class="contact-item indent">Lakemont, WA 98140</span>
      <span class="contact-item">
        www.bodyworkquietude.net
        <svg class="icon" viewBox="0 0 12 12" aria-hidden="true"><path d="M6 0a6 6 0 1 0 0 12A6 6 0 0 0 6 0zm0 1c.7 0 1.5 1.6 1.7 4H4.3C4.5 2.6 5.3 1 6 1zM4.3 6h3.4C7.5 8.4 6.7 11 6 11S4.5 8.4 4.3 6zM1 6h2.3c.1 1.7.4 3.2 1 4.2A5 5 0 0 1 1 6zm0-1a5 5 0 0 1 3.3-4.2c-.6 1-.9 2.5-1 4.2zm7.7 0c-.1-1.7-.4-3.2-1-4.2A5 5 0 0 1 11 5zm0 1H11a5 5 0 0 1-3.3 4.2c.6-1 .9-2.5 1-4.2z"/></svg>
      </span>
    </div>
  </section>

  <section class="card card--back">
    <div class="brand-name">Bodywork Quietude</div>
  </section>
</div>
</body>
</html>
```